Accounting and Financial Services Firm - Modern, Fresh, Original, Professional

We need a business card designed. We would like to see use of the the colors blue. Logo attached.

Modern, Fresh, Original, Professional,
Updates

Email section on business card required. design brief updated.

Target Market(s)

Small to medium businesses and high net worth individuals

Industry/Entity Type

Public Accounting

Contact Information for Business Card

Business Name: PM Ledgerline Chartered Accountants
Address: Level 14, 82 Harrow Lane Sydney NSW 2000
Ph: 02 9314 2587
Mobile: 04 XXXX XXXX
Email: anna@pmledgerline.com.au
Wechat ID: XXXXXXX
Website: www.pmledgerline.com.au

Name: Anna Petrov
Position: Manager

Font styles to use
Sans Serif

Colors
0492cd
33a6d7
85cae6

Requirements
Must have
• Modern font.

```html
<!DOCTYPE html>
<html lang="en">
<head>
<meta charset="utf-8">
<title>PM Ledgerline Business Card</title>
<link href="https://fonts.googleapis.com/css2?family=Lato:wght@400;700&display=swap" rel="stylesheet">
<style>
  :root {
    --brand-blue: #0492cd;
    --band-blue: #0a86bd;
    --mid-blue: #33a6d7;
    --light-blue: #85cae6;
    --ink: #2b2b2b;
    --paper: #ffffff;
    --backdrop: #3e3e3e;
  }
  * { margin: 0; padding: 0; box-sizing: border-box; }
  html, body { width: 1200px; height: 816px; overflow: hidden; }
  body {
    background: var(--backdrop);
    font-family: "Lato", Arial, sans-serif;
    display: flex;
    align-items: center;
    justify-content: center;
    gap: 40px;
  }
  .card {
    position: relative;
    width: 540px;
    height: 309px;
    background: var(--paper);
    box-shadow: 0 10px 24px rgba(0,0,0,0.45);
    overflow: hidden;
  }
  .card__band {
    height: 66px;
    background: var(--band-blue);
    color: var(--paper);
    display: flex;
    align-items: center;
    padding: 0 34px;
  }
  .card--front .card__band {
    justify-content: center;
    font-size: 22px;
    font-weight: 700;
  }
  .brand {
    display: flex;
    align-items: center;
    gap: 12px;
    color: var(--brand-blue);
    font-weight: 400;
    letter-spacing: 1px;
    text-transform: uppercase;
  }
  .brand__mark {
    width: 18px;
    height: 18px;
    background: var(--mid-blue);
  }
  .card--front .brand {
    position: absolute;
    left: 0; right: 0;
    top: 150px;
    justify-content: center;
    font-size: 34px;
  }
  .card--front .brand__mark { width: 26px; height: 26px; }
  .person__name { font-size: 24px; font-weight: 700; }
  .person__divider { margin: 0 10px; font-size: 22px; opacity: 0.85; }
  .person__role { font-size: 13px; }
  .card--back .brand {
    margin: 24px 0 0 34px;
    font-size: 20px;
  }
  .card--back .brand__mark { width: 14px; height: 14px; }
  .contact {
    margin: 20px 0 0 34px;
    border-collapse: collapse;
    font-size: 12.5px;
    color: var(--ink);
  }
  .contact th {
    text-align: left;
    font-weight: 400;
    padding: 1.5px 22px 1.5px 0;
  }
  .contact td { padding: 1.5px 0; }
</style>
</head>
<body>
  <section class="card card--front" aria-label="Business card front">
    <header class="card__band">PM Ledgerline Chartered Accountants</header>
    <div class="brand"><span class="brand__mark"></span>PM Ledgerline</div>
  </section>

  <section class="card card--back" aria-label="Business card back">
    <header class="card__band person">
      <span class="person__name">Anna Petrov</span>
      <span class="person__divider">|</span>
      <span class="person__role">Manager</span>
    </header>
    <div class="brand"><span class="brand__mark"></span>PM Ledgerline</div>
    <table class="contact">
      <tr><th>Address:</th><td>Level 14, 82 Harrow Lane Sydney NSW 2000</td></tr>
      <tr><th>Phone:</th><td>02 9314 2587</td></tr>
      <tr><th>Mobile:</th><td>04 XXXX XXXX</td></tr>
      <tr><th>Email:</th><td>anna@pmledgerline.com.au</td></tr>
      <tr><th>Wechat ID:</th><td>XXXXXXX</td></tr>
      <tr><th>Website:</th><td>www.pmledgerline.com.au</td></tr>
    </table>
  </section>
</body>
</html>
```